DMVN Website

Hi we require a website with similar attributes and design to this http://style5.tarnbridgepages.com but obviously with all our information and images etc... also attached are our logos please do the design with the yellow logo not the red.

```html
<!DOCTYPE html>
<html lang="en">
<head>
<meta charset="utf-8">
<title>DMVN Collision Repair Center</title>
<link href="https://fonts.googleapis.com/css2?family=Lato:wght@400;700;900&display=swap" rel="stylesheet">
<style>
:root{
  --yellow:#f2c300;
  --bg:#1b1b1b;
  --bg-alt:#232323;
  --panel:#2f2f2f;
  --line:#3a3a3a;
  --text:#ffffff;
  --muted:#b9b9b9;
  --gray-btn:#5b5b5b;
  --footer:#141414;
}
*{margin:0;padding:0;box-sizing:border-box}
html,body{width:1200px;height:2788px;overflow:hidden;background:var(--bg);font-family:"Lato",Arial,sans-serif;color:var(--text)}
a{color:inherit;text-decoration:none}
.page{position:relative;width:1200px;height:2788px}

/* buttons */
.btn{display:inline-block;white-space:nowrap;font-weight:700;font-size:15px;line-height:20px;padding:12px 0;width:150px;text-align:center;border-radius:4px}
.btn-yellow{background:var(--yellow);color:#111}
.btn-gray{background:var(--gray-btn);color:var(--text)}

/* section headings */
.heading{display:block;width:max-content;white-space:nowrap;padding:12px 34px;border:2px solid var(--yellow);border-radius:4px;background:#111;font-size:26px;line-height:32px;font-weight:900;letter-spacing:1px;color:var(--text)}
.centered{position:absolute;left:50%;transform:translateX(-50%)}

.bars{position:absolute;left:0;right:0;display:flex;justify-content:center;gap:8px}
.bars span{width:26px;height:4px;background:#666}
.bars span.on{background:var(--yellow)}

.social{display:flex;gap:14px}
.social span{width:16px;height:16px;border-radius:50%;background:var(--text);opacity:.85}

/* header + hero */
.hero{position:absolute;top:0;left:0;width:1200px;height:688px;overflow:hidden}
.hero-photo{position:absolute;inset:0;background:radial-gradient(ellipse at 30% 75%,#4a4d52 0%,rgba(0,0,0,0) 55%),radial-gradient(ellipse at 72% 45%,#5a5f66 0%,rgba(0,0,0,0) 50%),linear-gradient(180deg,#55585c 0%,#2c2e31 60%,#141618 100%)}
.topbar{position:absolute;top:0;left:0;right:0;height:56px;background:rgba(0,0,0,.6);display:flex;align-items:center;justify-content:space-between;padding:0 56px}
.phone{display:flex;align-items:center;gap:10px;font-size:17px;font-weight:700}
.phone svg{width:18px;height:18px}
.nav{position:absolute;top:144px;left:0;right:0;height:34px;background:rgba(0,0,0,.5)}
.nav a{position:absolute;top:8px;font-size:14px;line-height:18px;font-weight:700;letter-spacing:.5px;white-space:nowrap}
.nav a.active{color:var(--yellow)}
.logo{position:absolute;left:472px;top:36px;width:256px;height:144px;background:#141414;border:3px solid var(--yellow);border-top:none;border-radius:0 0 10px 10px;display:flex;align-items:center;justify-content:center;gap:12px}
.logo .mark{width:20px;height:20px;background:var(--yellow)}
.logo .name{font-size:30px;font-weight:900;color:var(--yellow);letter-spacing:1px}
.hero-title{position:absolute;top:330px;left:0;right:0;text-align:center;font-size:64px;font-weight:900;line-height:68px;letter-spacing:1px;text-shadow:0 2px 6px rgba(0,0,0,.6)}
.hero .btn{position:absolute;top:500px;left:525px}
.dots{position:absolute;top:636px;left:0;right:0;display:flex;justify-content:center;gap:8px}
.dots span{width:10px;height:10px;border-radius:50%;background:#888}
.dots span.on{background:var(--text)}

/* welcome */
.welcome{position:absolute;top:688px;left:0;width:1200px;height:400px;background:var(--bg-alt);text-align:center}
.welcome .heading{top:56px}
.welcome p{position:absolute;top:140px;left:220px;width:760px;font-size:14px;line-height:24px;color:var(--muted)}
.welcome .btn{position:absolute;top:306px;left:525px}

.divider{position:absolute;top:1088px;left:0;width:1200px;height:40px;background:var(--footer)}

/* services */
.services{position:absolute;top:1128px;left:0;width:1200px;height:552px;background:var(--bg)}
.services .heading{top:24px}
.cards{position:absolute;top:112px;left:72px;right:72px;display:flex;justify-content:space-between}
.card{width:320px;height:352px;background:var(--panel);border-radius:4px;overflow:hidden;text-align:center}
.card .photo{height:200px}
.card h3{margin:26px 0 10px;font-size:18px;line-height:22px;font-weight:900;color:var(--yellow);white-space:nowrap}
.card p{padding:0 30px;font-size:13px;line-height:20px;color:var(--muted)}
.services .bars{top:512px}

/* testimonials */
.testimonials{position:absolute;top:1680px;left:0;width:1200px;height:480px;background:var(--bg-alt);border-top:1px solid var(--line)}
.testimonials .heading{top:84px}
.quotes{position:absolute;top:168px;left:72px;right:60px;display:flex;justify-content:space-between}
.quote{width:510px;position:relative;padding-left:56px}
.quote .mark{position:absolute;left:0;top:-6px;font-size:60px;font-weight:900;color:var(--yellow);line-height:1}
.quote p{font-size:14px;line-height:24px;color:var(--muted)}
.author{display:flex;align-items:center;gap:22px;margin-top:20px}
.avatar{width:48px;height:48px;border-radius:50%;background:linear-gradient(160deg,#9a9a9a,#555)}
.author span{font-size:13px;font-weight:900;color:var(--yellow)}
.testimonials .bars{top:408px}

/* estimate */
.estimate{position:absolute;top:2160px;left:0;width:1200px;height:440px;background:linear-gradient(180deg,#3a1f1f 0%,#2b2b2b 40%,#1e1e1e 100%);overflow:hidden}
.estimate .bgphoto{position:absolute;inset:0;background:radial-gradient(ellipse at 20% 60%,rgba(150,60,50,.35),rgba(0,0,0,0) 50%),radial-gradient(ellipse at 85% 40%,rgba(120,120,120,.25),rgba(0,0,0,0) 50%)}
.estimate .heading{top:50px;z-index:2}
.form{position:absolute;top:128px;left:248px;width:704px}
.row{display:flex;justify-content:space-between;margin-bottom:14px}
.field{width:332px;height:44px;background:#fff;border-radius:4px;color:#666;font-size:14px;line-height:20px;padding:12px 16px}
.field.message{width:704px;height:100px}
.form .btn{display:block;margin:14px auto 0}

/* footer */
.footer{position:absolute;top:2600px;left:0;width:1200px;height:188px;background:var(--footer);text-align:center}
.footer nav{position:absolute;top:52px;left:0;right:0;display:flex;justify-content:center;gap:40px;font-size:13px;line-height:18px;font-weight:700}
.footer .copy{position:absolute;top:84px;left:0;right:0;font-size:13px;line-height:18px;color:var(--muted)}
.footer .social{position:absolute;top:118px;left:0;right:0;justify-content:center}
</style>
</head>
<body>
<div class="page">

  <header class="hero">
    <div class="hero-photo" role="img" aria-label="Photo of technicians discussing a repaired black sedan in a body shop"></div>
    <div class="topbar">
      <div class="social" aria-label="Social links"><span></span><span></span><span></span><span></span><span></span></div>
      <div class="phone">
        <svg viewBox="0 0 24 24"><path fill="#f2c300" d="M6.6 10.8a15 15 0 0 0 6.6 6.6l2.2-2.2a1 1 0 0 1 1-.25 11.4 11.4 0 0 0 3.6.57 1 1 0 0 1 1 1V20a1 1 0 0 1-1 1A17 17 0 0 1 3 4a1 1 0 0 1 1-1h3.5a1 1 0 0 1 1 1c0 1.25.2 2.45.57 3.57a1 1 0 0 1-.25 1z"/></svg>
        1-800-555-0148
      </div>
    </div>
    <nav class="nav">
      <a href="#" class="active" style="left:72px">HOME</a>
      <a href="#" style="left:160px">ABOUT US</a>
      <a href="#" style="left:288px">SERVICES</a>
      <a href="#" style="left:400px">BLOG</a>
      <a href="#" style="left:784px">TESTIMONIALS</a>
      <a href="#" style="left:930px">CAREERS</a>
      <a href="#" style="left:1034px">CONTACT US</a>
    </nav>
    <div class="logo"><span class="mark"></span><span class="name">DMVN</span></div>
    <h1 class="hero-title">DMVN COLLISION<br>REPAIR CENTER</h1>
    <a href="#" class="btn btn-yellow">READ MORE</a>
    <div class="dots"><span class="on"></span><span></span><span></span><span></span></div>
  </header>

  <section class="welcome">
    <h2 class="heading centered">WELCOME TO YOUR WEBSITE</h2>
    <p>Lorem ipsum dolor sit amet, consectetur adipiscing elit. Donec sed nibh neque. Donec congue maximus nibh id dignissim. Maecenas turpis dui, porta in nulla feugiat, pellentesque cursus orci. Fusce quis nunc risus. Vivamus pellentesque quis augue sed sollicitudin. Fusce scelerisque, leo eget dapibus maximus, ipsum turpis consectetur diam, commodo fringilla risus quam et lectus. Donec feugiat lectus iaculis commodo dignissim. Aliquam metus sapien, commodo vitae enim ac, malesuada vestibulum tellus. In ac arcu id ligula sed consequat placerat sed et lobortis.</p>
    <a href="#" class="btn btn-gray">READ MORE</a>
  </section>

  <div class="divider"></div>

  <section class="services">
    <h2 class="heading centered">OUR SERVICES</h2>
    <div class="cards">
      <article class="card">
        <div class="photo" role="img" aria-label="Photo of a technician repairing a blue car body panel" style="background:linear-gradient(135deg,#2c4f8a,#6d7c92 60%,#3a3a3a)"></div>
        <h3>AUTO BODY REPAIR</h3>
        <p>Lorem ipsum dolor sit amet, consectetur adipiscing elit sed nibh neque congue maximus nibh id dignissim.</p>
      </article>
      <article class="card">
        <div class="photo" role="img" aria-label="Photo of a painter refinishing a car in a spray booth" style="background:linear-gradient(135deg,#8a8d90,#4f5458 55%,#2b2e31)"></div>
        <h3>AUTO BODY REFINISHING</h3>
        <p>Lorem ipsum dolor sit amet, consectetur adipiscing elit sed nibh neque congue maximus nibh id dignissim.</p>
      </article>
      <article class="card">
        <div class="photo" role="img" aria-label="Photo of a worker polishing a blue car with a buffer" style="background:linear-gradient(135deg,#3d6fb3,#8f3b33 55%,#2e2e2e)"></div>
        <h3>AUTOMOTIVE DETAILING</h3>
        <p>Lorem ipsum dolor sit amet, consectetur adipiscing elit sed nibh neque congue maximus nibh id dignissim.</p>
      </article>
    </div>
    <div class="bars"><span class="on"></span><span></span><span></span></div>
  </section>

  <section class="testimonials">
    <h2 class="heading centered">TESTIMONIALS</h2>
    <div class="quotes">
      <blockquote class="quote">
        <span class="mark">&ldquo;</span>
        <p>&ldquo; Lorem ipsum dolor sit amet, consectetur adipiscing elit. Donec sed nibh neque. Donec congue maximus nibh id dignissim. Maecenas turpis dui, porta in nulla feugiat, pellentesque cursus orci quis nunc risus. Vivamus pellentesque quis augue sed sollicitudin. &rdquo;</p>
        <div class="author"><span class="avatar" role="img" aria-label="Customer portrait photo"></span><span>NAME HEADING</span></div>
      </blockquote>
      <blockquote class="quote">
        <span class="mark">&ldquo;</span>
        <p>&ldquo; Lorem ipsum dolor sit amet, consectetur adipiscing elit. Donec sed nibh neque. Donec congue maximus nibh id dignissim. Maecenas turpis dui, porta in nulla feugiat, pellentesque cursus orci quis nunc risus. Vivamus pellentesque quis augue sed sollicitudin. &rdquo;</p>
        <div class="author"><span class="avatar" role="img" aria-label="Customer portrait photo"></span><span>NAME HEADING</span></div>
      </blockquote>
    </div>
    <div class="bars"><span class="on"></span><span></span><span></span></div>
  </section>

  <section class="estimate">
    <div class="bgphoto" role="img" aria-label="Dimmed photo of hands working on a car engine"></div>
    <h2 class="heading centered">GET AN ONLINE ESTIMATE</h2>
    <form class="form">
      <div class="row"><div class="field">Name</div><div class="field">Email Address</div></div>
      <div class="row"><div class="field">Phone No</div><div class="field">Subject</div></div>
      <div class="row"><div class="field message">Message</div></div>
      <a href="#" class="btn btn-gray">SUBMIT NOW</a>
    </form>
  </section>

  <footer class="footer">
    <nav>
      <a href="#">HOME</a><a href="#">ABOUT US</a><a href="#">SERVICES</a><a href="#">BLOG</a><a href="#">TESTIMONIALS</a><a href="#">CAREERS</a><a href="#">CONTACT US</a>
    </nav>
    <p class="copy">Copyright &copy; 2018, Company Name. All Rights Reserved</p>
    <div class="social"><span></span><span></span><span></span><span></span><span></span></div>
  </footer>

</div>
</body>
</html>
```